Healthy Lifestyle Vitamin Supplement Company needs a web site designed.

We are starting a new website for selling quality natural vitamins and supplements online plus providing news and information on healthy living. We DO NOT need any programming done for this site. Just the design in a layered photoshop file. This site needs to communicate that we are the authoritative source for healthy living and a trusted place to buy supplements and information on living a healthy lifestyle.

Triggers On page will be

Trigger set 1
Home - Shop By Brand - Top Sellers - Clearance - Help Center - My Favorites

Trigger set 2
Vitamins and Herbs - Natural Living - Aromatherapy - Coffee and Tea - Health and Beauty - Healthy Foods - Pet Health - Sports and Diet

Triggers Other
Login - Shopping Cart - Checkout - Track Order

Need a search bar in the design

Left side should be categories look at Verolane.com for example of categories.

Name and domain name is Brisk Meadow Crest

Will also need a logo to go along with that.

```html
<!DOCTYPE html>
<html lang="en">
<head>
<meta charset="utf-8">
<title>Brisk Meadow Crest – Natural Vitamins &amp; Supplements</title>
<link rel="stylesheet" href="https://fonts.googleapis.com/css2?family=Open+Sans:wght@400;600;700;800&display=swap">
<style>
:root{
  --ink:#333333;
  --muted:#8a8a8a;
  --line:#e3e3e3;
  --green:#9cc21b;
  --orange:#f07f1b;
  --taupe:#b3ad98;
  --topbar:#2a2a2a;
  --hero-panel:#4a4540;
  --footer:#3b2f27;
  --footer-base:#2e2a27;
  --white:#ffffff;
  --page:#ffffff;
}
*{box-sizing:border-box;margin:0;padding:0}
html,body{width:1200px;height:2470px;overflow:hidden}
body{position:relative;background:var(--page);font-family:"Open Sans",Arial,sans-serif;color:var(--ink);font-size:12px}
.abs{position:absolute}
a{color:inherit;text-decoration:none}

/* top bar */
.topbar{left:0;top:0;width:1200px;height:45px;background:var(--topbar);color:#ddd;font-size:12px}
.topbar span{position:absolute;top:14px;display:flex;align-items:center;gap:7px;white-space:nowrap}
.topbar svg{width:14px;height:14px}

/* header */
.logo{left:97px;top:70px;display:flex;align-items:center;gap:10px}
.logo-dot{width:48px;height:48px;border-radius:50%;background:var(--green)}
.logo-name{font-size:27px;font-weight:600;color:#5a5a5a;letter-spacing:-.3px}
.nav{right:136px;top:94px;display:flex;gap:19px;font-size:12px;font-weight:700;text-transform:uppercase;color:#444;white-space:nowrap}
.search-icon{left:1088px;top:95px;width:14px;height:14px}

/* hero */
.hero-photo{left:97px;top:148px;width:638px;height:352px;background:linear-gradient(100deg,#d9b294 0%,#c9c3ad 35%,#7fb59a 60%,#c9d7cf 100%)}
.hero-panel{left:735px;top:148px;width:372px;height:352px;background:var(--hero-panel);color:var(--white);text-align:center}
.hero-panel h1{margin-top:80px;font-size:33px;font-weight:700;letter-spacing:.5px}
.hero-panel hr{width:200px;margin:16px auto 20px;border:0;border-top:1px solid #fff}
.hero-panel p{width:270px;margin:0 auto;font-size:12.5px;line-height:21px}
.btn-green{display:inline-block;background:var(--green);color:#fff;font-weight:700;font-size:12px;padding:9px 16px;text-transform:uppercase}
.hero-panel .btn-green{margin-top:26px}

/* sidebar */
.side-title{font-size:17px;font-weight:700;text-transform:uppercase;color:#2d2d2d;white-space:nowrap}
.cat-list{left:97px;top:565px;width:215px;list-style:none}
.cat-list li{font-size:12px;text-transform:uppercase;color:#555;padding:10px 16px;border-bottom:1px solid var(--line)}
.cat-list li.active{color:var(--green);font-weight:600}
.arrows{display:flex;gap:4px}
.arrows i{width:26px;height:26px;background:#eeeeee;display:flex;align-items:center;justify-content:center}
.arrows svg{width:10px;height:10px}

/* product bits */
.pname{font-size:12px;font-weight:700;text-transform:uppercase;text-align:center}
.pline{width:46px;height:3px;background:var(--green);margin:9px auto}
.pdesc{font-size:10px;color:var(--muted);text-align:center;line-height:14px}
.price{display:flex;width:122px;height:34px;margin:16px auto 0;border:1px solid #d8d8d8}
.price b{flex:1;display:flex;align-items:center;justify-content:center;color:var(--orange);font-size:14px;font-weight:700}
.price i{width:34px;background:var(--taupe);display:flex;align-items:center;justify-content:center}
.price svg{width:16px;height:16px}
.shot{margin:0 auto}

.card{width:220px;height:313px;border:1px solid var(--line);background:#fff;padding-top:70px}
.card .shot{position:absolute;left:55px;top:25px;width:110px;height:150px;border-radius:10px}
.card .pname{margin-top:125px}
.tag{position:absolute;left:8px;top:8px;padding:4px 10px;font-size:10px;font-weight:700;color:#fff;background:var(--orange)}
.tag.green{background:var(--green)}

/* section header */
.sec-head{font-size:17px;font-weight:700;text-transform:uppercase;white-space:nowrap}
.tabs{right:93px;width:500px;font-size:9.5px;color:var(--muted);display:flex;justify-content:flex-end;gap:4px;white-space:nowrap}
.tabs b{font-weight:600;color:#555}

/* promo */
.promo{left:354px;top:540px;width:753px;height:260px;background:#fff;box-shadow:0 0 0 1px #f0f0f0}
.promo-label{left:23px;top:0;width:222px;height:38px;background:var(--green);color:#fff;font-weight:700;font-size:16px;display:flex;align-items:center;justify-content:center;text-transform:uppercase}
.btn-ghost{display:inline-block;border:1px solid #cfcfcf;padding:9px 22px;font-size:11px;font-weight:600;letter-spacing:1px;text-transform:uppercase;color:#555}

/* banner */
.view-more{left:354px;top:1624px;width:753px;height:40px;background:#2f2f2f;color:#fff;font-size:12px;font-weight:700;display:flex;align-items:center;justify-content:center;text-transform:uppercase}
.banner-left{left:354px;top:1692px;width:300px;height:123px;background:linear-gradient(90deg,#2f3a2b,#4a5a3a)}
.banner-right{left:654px;top:1692px;width:453px;height:123px;background:linear-gradient(90deg,#5a3a14,#b4741d 45%,#e0b25a 75%,#c9d2c6)}
.banner-text{left:376px;top:1712px;color:#fff;font-size:23px;line-height:25px;font-weight:400;text-transform:uppercase}
.banner-text b{color:var(--green);font-weight:700}

/* bottom info */
.news-title{font-size:12px;font-weight:700;text-transform:uppercase}
.body-copy{font-size:11px;line-height:17px;color:#666}
.tweet{display:flex;gap:20px}
.tweet .bird{width:42px;height:42px;border-radius:50%;background:var(--green);flex:none;display:flex;align-items:center;justify-content:center}
.tweet .bird i{width:14px;height:14px;border-radius:50%;background:#fff}
.tweet .who{color:var(--green);font-weight:700}
.video{left:780px;top:1893px;width:300px;height:187px;background:linear-gradient(135deg,#5b3a23,#8a6a4b 50%,#3e2a1c)}
.play{left:899px;top:1955px;width:60px;height:60px;border-radius:50%;background:#fff;display:flex;align-items:center;justify-content:center}

/* footer */
.footer{left:0;top:2178px;width:1200px;height:226px;background:linear-gradient(90deg,#3d2e24,#4a392b 50%,#3a2c22)}
.foot-col{position:absolute;top:50px;color:#e8e2da}
.foot-col h4{font-size:12px;font-weight:700;text-transform:uppercase;color:#fff;margin-bottom:12px}
.foot-col li{list-style:none;font-size:11px;line-height:23px}
.signup{display:flex;margin-top:20px}
.signup span{width:178px;height:34px;border:1px solid #fff;display:flex;align-items:center;justify-content:center;font-size:11px}
.signup b{width:68px;height:34px;background:var(--green);color:#fff;display:flex;align-items:center;justify-content:center;font-size:11px}
.social{display:flex;gap:8px}
.social i{width:20px;height:20px;border-radius:50%;background:#fff}
.cards{display:flex;gap:6px}
.cards i{width:30px;height:18px;background:#fff;border-radius:2px}
.base{left:0;top:2404px;width:1200px;height:66px;background:var(--footer-base);color:#ddd;font-size:11px}
</style>
</head>
<body>

<!-- top bar -->
<div class="abs topbar">
  <span style="left:93px">Corin Hale, welcome to our online store!</span>
  <span style="left:460px"><svg viewBox="0 0 16 16"><circle cx="8" cy="8" r="8" fill="#ddd"/><path d="M5 4l2 1-1 2 3 3 2-1 1 2-2 1C7 12 4 9 4 6z" fill="#2a2a2a"/></svg>+621 555 0147</span>
  <span style="left:598px"><svg viewBox="0 0 16 16"><circle cx="8" cy="8" r="8" fill="#ddd"/><rect x="4" y="5" width="8" height="6" fill="#2a2a2a"/></svg>info@briskmeadowcrest.com</span>
  <span style="left:800px">Login</span>
  <span style="left:858px"><svg viewBox="0 0 16 16"><circle cx="8" cy="5" r="3" fill="#ddd"/><path d="M2 15c0-4 3-6 6-6s6 2 6 6z" fill="#ddd"/></svg>My Account ⌄</span>
  <span style="left:978px"><svg viewBox="0 0 16 16"><path d="M1 2h3l2 8h8l2-6H5" stroke="#ddd" fill="none" stroke-width="1.6"/><circle cx="7" cy="13" r="1.5" fill="#ddd"/><circle cx="13" cy="13" r="1.5" fill="#ddd"/></svg>0 item</span>
  <span style="left:1058px">Checkout</span>
</div>

<!-- header -->
<div class="abs logo"><i class="logo-dot"></i><span class="logo-name">Brisk Meadow Crest</span></div>
<nav class="abs nav"><a>Home</a><a>Shop by Brand</a><a>Top Sellers</a><a>Clearance</a><a>Help Center</a><a>My Favorites</a></nav>
<svg class="abs search-icon" viewBox="0 0 16 16"><circle cx="6.5" cy="6.5" r="5" stroke="#444" stroke-width="2" fill="none"/><path d="M10 10l5 5" stroke="#444" stroke-width="2"/></svg>

<!-- hero -->
<div class="abs hero-photo" role="img" aria-label="Smiling woman holding a supplement bottle in a store aisle"></div>
<div class="abs hero-panel">
  <h1>LOREM IPSUMEI</h1>
  <hr>
  <p>aspernatur magni quae aperiam aut veritatis beatae eos aut voluptas doloremque perspiciatis error natus natus aut eaque inventore quasi consequuntur consequuntur quae aspernatur site sit</p>
  <a class="btn-green">View More</a>
</div>

<!-- sidebar: categories -->
<div class="abs side-title" style="left:105px;top:540px">Shop by Category</div>
<ul class="abs cat-list">
  <li>Vitamins and Herbs</li><li class="active">Natural Living</li><li>Aromatherapy</li><li>Coffee and Tea</li>
  <li>Health and Beauty</li><li>Healthy Foods</li><li>Pet Health</li><li style="border:0">Sports and Diet</li>
</ul>

<!-- sidebar: best seller -->
<div class="abs side-title" style="left:105px;top:940px">Best Seller</div>
<div class="abs arrows" style="left:255px;top:937px"><i><svg viewBox="0 0 10 10"><path d="M7 1L3 5l4 4" stroke="#aaa" fill="none"/></svg></i><i><svg viewBox="0 0 10 10"><path d="M3 1l4 4-4 4" stroke="#aaa" fill="none"/></svg></i></div>
<div class="abs" style="left:97px;top:990px;width:225px">
  <div class="shot" role="img" aria-label="Two bottles of aloe coconut drink" style="width:100px;height:190px;background:linear-gradient(180deg,#f4a95a,#f2efe6 40%,#cfe0b3)"></div>
  <div class="pname" style="margin-top:12px">Voluptatem Fugit Aut</div><div class="pline"></div>
  <div class="pdesc">ut nemo nem ipsam quasi voluptates<br>doloremque qui aut eaque</div>
  <div class="price"><b>$856.00</b><i><svg viewBox="0 0 16 16"><path d="M1 2h3l2 8h8l2-6H5" stroke="#fff" fill="none" stroke-width="1.6"/><circle cx="7" cy="13" r="1.5" fill="#fff"/><circle cx="13" cy="13" r="1.5" fill="#fff"/></svg></i></div>
</div>

<!-- sidebar: special offer -->
<div class="abs side-title" style="left:105px;top:1382px">Special Offer</div>
<div class="abs arrows" style="left:255px;top:1380px"><i><svg viewBox="0 0 10 10"><path d="M7 1L3 5l4 4" stroke="#aaa" fill="none"/></svg></i><i><svg viewBox="0 0 10 10"><path d="M3 1l4 4-4 4" stroke="#aaa" fill="none"/></svg></i></div>
<div class="abs" style="left:97px;top:1448px;width:225px">
  <div class="shot" role="img" aria-label="Orange and white fish oil supplement tub" style="width:100px;height:160px;border-radius:12px;background:linear-gradient(180deg,#e0541d 0 18%,#f4f1ea 18% 40%,#f08a1c 40% 80%,#f4f1ea 80%)"></div>
  <div class="pname" style="margin-top:30px">Voluptatem Fugit Aut</div><div class="pline"></div>
  <div class="pdesc">ut nemo nem ipsam quasi voluptates<br>doloremque qui aut eaque</div>
  <div class="price"><b>$856.00</b><i><svg viewBox="0 0 16 16"><path d="M1 2h3l2 8h8l2-6H5" stroke="#fff" fill="none" stroke-width="1.6"/><circle cx="7" cy="13" r="1.5" fill="#fff"/><circle cx="13" cy="13" r="1.5" fill="#fff"/></svg></i></div>
</div>

<!-- promo -->
<section class="abs promo">
  <div class="abs promo-label">Promo of the Month</div>
  <div class="abs" style="left:30px;top:78px;width:180px;text-align:center">
    <div class="pname">Voluptatem Fugit Aut</div>
    <div style="color:var(--green);font-size:17px;font-weight:700;margin:12px 0 6px">$380.00</div>
    <div class="pdesc" style="font-size:9px;line-height:12px">ut nemo nem ipsam quasi voluptates<br>doloremque qui aut eaque ut minus<br>nisi rem aperiam aut eaque est</div>
    <a class="btn-ghost" style="margin-top:12px">Read More</a>
  </div>
  <div class="abs" role="img" aria-label="Three vitamin C and fish oil supplement jars" style="left:306px;top:30px;width:362px;height:212px;border-radius:14px;background:linear-gradient(180deg,#e2b54a 0 12%,#3b2a1a 12% 30%,#e87a20 30% 70%,#2e4a1a 70%)"></div>
  <div class="abs arrows" style="left:683px;top:0"><i><svg viewBox="0 0 10 10"><path d="M7 1L3 5l4 4" stroke="#aaa" fill="none"/></svg></i><i><svg viewBox="0 0 10 10"><path d="M3 1l4 4-4 4" stroke="#aaa" fill="none"/></svg></i></div>
</section>

<!-- new products -->
<div class="abs sec-head" style="left:366px;top:842px">New Product</div>
<div class="abs tabs" style="top:847px"><span>Aspernatur Magni</span>|<b>Quas Aperiam Aut</b>|<span>Veritatis Beatae Eos</span>|<span>Aut Voluptas Doloremque</span>|<span>Perspiciatis</span></div>

<div class="abs card" style="left:366px;top:885px"><span class="tag">NEW</span><div class="shot" role="img" aria-label="Purple and white prenatal vitamin bottle" style="background:linear-gradient(180deg,#2a2a40 0 18%,#f3f0f5 18% 45%,#7a4a9a 45% 70%,#f3f0f5 70%)"></div><div class="pname">Voluptatem Fugit Aut</div><div class="pline"></div><div class="pdesc">ut nemo nem ipsam quasi voluptates<br>doloremque qui aut eaque</div><div class="price"><b>$856.00</b><i><svg viewBox="0 0 16 16"><path d="M1 2h3l2 8h8l2-6H5" stroke="#fff" fill="none" stroke-width="1.6"/><circle cx="7" cy="13" r="1.5" fill="#fff"/><circle cx="13" cy="13" r="1.5" fill="#fff"/></svg></i></div></div>
<div class="abs card" style="left:617px;top:885px"><span class="tag green">10%</span><div class="shot" role="img" aria-label="Dark herbal tea supplement bottle with green label" style="background:linear-gradient(180deg,#2a1a10 0 20%,#5a3a1a 20% 40%,#7aa63a 40% 80%,#2a1a10 80%)"></div><div class="pname">Voluptatem Fugit Aut</div><div class="pline"></div><div class="pdesc">ut nemo nem ipsam quasi voluptates<br>doloremque qui aut eaque</div><div class="price"><b>$856.00</b><i><svg viewBox="0 0 16 16"><path d="M1 2h3l2 8h8l2-6H5" stroke="#fff" fill="none" stroke-width="1.6"/><circle cx="7" cy="13" r="1.5" fill="#fff"/><circle cx="13" cy="13" r="1.5" fill="#fff"/></svg></i></div></div>
<div class="abs card" style="left:873px;top:885px"><span class="tag">NEW</span><div class="shot" role="img" aria-label="Blue prostate support supplement bottle" style="background:linear-gradient(180deg,#1a2a8a 0 25%,#2a4ac8 25% 85%,#1a2a8a 85%)"></div><div class="pname">Voluptatem Fugit Aut</div><div class="pline"></div><div class="pdesc">ut nemo nem ipsam quasi voluptates<br>doloremque qui aut eaque</div><div class="price"><b>$856.00</b><i><svg viewBox="0 0 16 16"><path d="M1 2h3l2 8h8l2-6H5" stroke="#fff" fill="none" stroke-width="1.6"/><circle cx="7" cy="13" r="1.5" fill="#fff"/><circle cx="13" cy="13" r="1.5" fill="#fff"/></svg></i></div></div>

<!-- featured products -->
<div class="abs sec-head" style="left:366px;top:1253px">Featured Products</div>
<div class="abs tabs" style="top:1258px"><span>Aspernatur Magni</span>|<b>Quas Aperiam Aut</b>|<span>Veritatis Beatae Eos</span>|<span>Aut Voluptas Doloremque</span>|<span>Perspiciatis</span></div>

<div class="abs card" style="left:366px;top:1290px"><span class="tag">NEW</span><div class="shot" role="img" aria-label="White garcinia supplement bottle with green label" style="background:linear-gradient(180deg,#e8ece4 0 20%,#6aa63a 20% 70%,#f0f0ea 70%)"></div><div class="pname">Voluptatem Fugit Aut</div><div class="pline"></div><div class="pdesc">ut nemo nem ipsam quasi voluptates<br>doloremque qui aut eaque</div><div class="price"><b>$856.00</b><i><svg viewBox="0 0 16 16"><path d="M1 2h3l2 8h8l2-6H5" stroke="#fff" fill="none" stroke-width="1.6"/><circle cx="7" cy="13" r="1.5" fill="#fff"/><circle cx="13" cy="13" r="1.5" fill="#fff"/></svg></i></div></div>
<div class="abs card" style="left:617px;top:1290px"><div class="shot" role="img" aria-label="White supplement bottle with green leaf label" style="background:linear-gradient(180deg,#e4e4e4 0 20%,#f7f7f7 20% 45%,#4a8a3a 45% 70%,#f7f7f7 70%)"></div><div class="pname">Voluptatem Fugit Aut</div><div class="pline"></div><div class="pdesc">ut nemo nem ipsam quasi voluptates<br>doloremque qui aut eaque</div><div class="price"><b>$856.00</b><i><svg viewBox="0 0 16 16"><path d="M1 2h3l2 8h8l2-6H5" stroke="#fff" fill="none" stroke-width="1.6"/><circle cx="7" cy="13" r="1.5" fill="#fff"/><circle cx="13" cy="13" r="1.5" fill="#fff"/></svg></i></div></div>
<div class="abs card" style="left:873px;top:1290px"><span class="tag">NEW</span><div class="shot" role="img" aria-label="Chromium picolinate bottle with yellow label" style="background:linear-gradient(180deg,#f0f0ea 0 20%,#e8c22a 20% 75%,#f0f0ea 75%)"></div><div class="pname">Voluptatem Fugit Aut</div><div class="pline"></div><div class="pdesc">ut nemo nem ipsam quasi voluptates<br>doloremque qui aut eaque</div><div class="price"><b>$856.00</b><i><svg viewBox="0 0 16 16"><path d="M1 2h3l2 8h8l2-6H5" stroke="#fff" fill="none" stroke-width="1.6"/><circle cx="7" cy="13" r="1.5" fill="#fff"/><circle cx="13" cy="13" r="1.5" fill="#fff"/></svg></i></div></div>

<a class="abs view-more">View More Items</a>

<!-- banner -->
<div class="abs banner-left" role="img" aria-label="Dark green leafy background"></div>
<div class="abs banner-right" role="img" aria-label="Cup of honey tea with lemon slice"></div>
<div class="abs banner-text"><b>Max</b>imize<br>your<br>healty</div>
<div class="abs" style="left:505px;top:1716px;width:1px;height:62px;background:#cfd6c4"></div>
<div class="abs" style="left:518px;top:1722px;width:120px;color:#dfe5d4;font-size:9px;line-height:13px">lorem nem ipsam quasi<br>voluptates qui aut<br>eaque est ipsum ut<br>aperiam aut dolor</div>
<div class="abs" style="left:376px;top:1795px;display:flex;gap:4px"><i style="width:6px;height:6px;border-radius:50%;background:#fff"></i><i style="width:6px;height:6px;border-radius:50%;background:#8a927e"></i><i style="width:6px;height:6px;border-radius:50%;background:#8a927e"></i><i style="width:6px;height:6px;border-radius:50%;background:#8a927e"></i><i style="width:6px;height:6px;border-radius:50%;background:#8a927e"></i></div>

<!-- latest news -->
<div class="abs side-title" style="left:105px;top:1857px">Lates News</div>
<div class="abs arrows" style="left:353px;top:1855px"><i><svg viewBox="0 0 10 10"><path d="M7 1L3 5l4 4" stroke="#aaa" fill="none"/></svg></i><i><svg viewBox="0 0 10 10"><path d="M3 1l4 4-4 4" stroke="#aaa" fill="none"/></svg></i></div>
<div class="abs" style="left:105px;top:1898px;width:255px">
  <div class="news-title">Lorem ipsum dolor sit amet rem eos</div>
  <div class="body-copy" style="margin:6px 0 10px;font-size:10px">May 16, 2014</div>
  <p class="body-copy">Lorem ipsum dolor sit amet voluptatem fugit aut illo explicabo nemo rem ipsam quasi illo dolores voluptatem doloremque perspiciatis beatae magni architecto odit aspernatur magni quae aperiam aut qui aut eaque inventore aut quasi consequuntur consequuntur ipsa</p>
  <div style="color:var(--green);font-size:10px;margin-top:18px">read more</div>
</div>

<!-- tweets -->
<div class="abs side-title" style="left:442px;top:1857px">Tweets</div>
<div class="abs" style="left:452px;top:1893px;width:290px">
  <div class="tweet"><i class="bird"><i></i></i><div class="body-copy" style="font-size:10.5px"><span class="who">Tam Reyes</span> @Corin Hale<br>Lorem ipsum dolor sit amet voluptatem fugit aut omnis explicabo ipsa nemo rem ipsam<br><span style="line-height:34px">retweeted by <span class="who">Lina Voss</span></span></div></div>
  <div class="tweet" style="margin-top:12px"><i class="bird"><i></i></i><div class="body-copy" style="font-size:10.5px"><span class="who">Tam Reyes</span> @Corin Hale<br>Lorem ipsum dolor sit amet voluptatem fugit aut omnis explicabo ipsa nemo rem ipsam<br><span style="line-height:34px">retweeted by <span class="who">Lina Voss</span></span></div></div>
</div>

<!-- why choose us -->
<div class="abs side-title" style="left:783px;top:1857px">Why You Choose Us</div>
<div class="abs video" role="img" aria-label="Pile of herbal supplement tablets on a wooden spoon"></div>
<div class="abs play"><svg width="22" height="22" viewBox="0 0 22 22"><path d="M6 3l14 8-14 8z" fill="#333"/></svg></div>

<!-- footer -->
<footer class="abs footer">
  <div class="foot-col" style="left:92px"><h4>Company</h4><ul><li>Search</li><li>About</li><li>News</li><li>Retailers</li><li>Contact Us</li></ul></div>
  <div class="foot-col" style="left:265px"><h4>Shipping</h4><ul><li>Shipping Fee</li><li>Order and Returns</li><li>Track Order</li><li>Search Term</li><li>Site Map</li></ul></div>
  <div class="foot-col" style="left:440px"><h4>FAQs</h4><ul><li>Customers Service</li><li>Privacy Policy</li><li>Term and Use</li><li>My Account</li><li>Others</li></ul></div>
  <div class="foot-col" style="left:613px"><h4>News &amp; Updates</h4><div style="font-size:11px">Sign up to get the latest on sales, new releases and more ...</div>
    <div class="signup" style="margin-top:34px"><span>enter your email here</span><b>SIGN UP</b></div></div>
  <div class="foot-col" style="left:962px"><h4>Follow Us Now</h4><div class="social"><i></i><i></i><i></i><i></i><i></i></div>
    <div style="width:140px;height:1px;background:#8a7a6a;margin:14px 0"></div>
    <h4 style="margin-bottom:10px">Payment Method</h4><div class="cards"><i></i><i></i><i></i><i></i></div></div>
</footer>
<div class="abs base">
  <span class="abs" style="left:90px;top:26px">© 2014 <b>Brisk Meadow Crest</b></span>
  <span class="abs" style="left:686px;top:26px;display:flex;gap:18px"><a>About us</a><a>privacy policy</a><a>terms and use</a><a>Careers</a><a>Countries</a><a>contact us</a></span>
</div>

</body>
</html>
```